Crestline 14 Industrial Park Needs Website

We are looking for a website for a new project we are working on.
Project does not have a logo so just use text. Needs to be responsive and mobile friendly for all browsers and coded for both Android & IOS. SEO is also important. Want something visually grabbing that displays growth, quality and confidence.
WordPress or Joomla – must be desktop and mobile friendly with fast page load speed. Need the ability to edit ourselves.
See attached website brief for further information.
Land Sale/Lease/Development
Coded - Design and coding required
4 page

```html
<!DOCTYPE html>
<html lang="en">
<head>
<meta charset="utf-8">
<meta name="viewport" content="width=1200">
<title>Crestline 14 Industrial Park – St. Paul, Alberta</title>
<link rel="stylesheet" href="https://fonts.googleapis.com/css2?family=Cinzel:wght@500;600;700&family=Poppins:wght@400;500;600&display=swap">
<style>
:root{
  --ink:#1d1d1f;
  --muted:#3a3a3c;
  --brand:#0b55ad;
  --brand-soft:#7ea7db;
  --panel:#e6eef8;
  --hero-a:#24406a;
  --hero-b:#5e7592;
  --footer:#0b0b0b;
  --footer-box:#1d1d1d;
  --white:#ffffff;
}
*{box-sizing:border-box;margin:0;padding:0}
html,body{width:1200px;height:4761px;overflow:hidden;background:var(--white)}
body{font-family:"Poppins",sans-serif;color:var(--ink);position:relative}
.serif{font-family:"Cinzel",serif}
section,header,footer{position:absolute;left:0;width:1200px}
.abs{position:absolute}
.title{font-family:"Cinzel",serif;font-weight:600;font-size:40px;line-height:48px;color:var(--ink);text-align:center}
.body{font-size:12.5px;line-height:18.5px;color:var(--muted)}
.btn{position:absolute;display:flex;align-items:center;justify-content:center;gap:14px;font-size:10.5px;font-weight:500;color:var(--white)}
.btn svg{width:18px;height:8px}
.btn-dark{background:var(--brand)}
.btn-soft{background:var(--brand-soft)}
.email{position:absolute;display:flex;align-items:center;gap:14px}
.email .ring{width:30px;height:30px;border-radius:50%;border:1px solid var(--brand-soft);display:flex;align-items:center;justify-content:center}
.email small{display:block;font-size:8.5px;line-height:10px}
.email strong{display:block;font-family:"Cinzel",serif;font-weight:700;font-size:14px;line-height:18px}
.vsep{position:absolute;width:1px;height:22px;background:#c7c7cc}
.photo{position:absolute}

/* hero */
.hero{top:0;height:562px;background:linear-gradient(180deg,#3c5a82 0%,#5d7590 45%,#3f546f 100%)}
.hero .shade{position:absolute;inset:0;background:linear-gradient(90deg,rgba(30,55,95,.75) 0%,rgba(40,70,110,.35) 60%,rgba(30,50,80,.2) 100%)}
.logo{font-family:"Cinzel",serif;font-weight:700;font-size:21px;color:var(--white);letter-spacing:.5px}
.nav{position:absolute;top:32px;right:110px;display:flex;gap:34px;font-size:11px;color:var(--white)}
.nav .on{font-weight:600;border-bottom:1.5px solid var(--white);padding-bottom:3px}
.hero h1{position:absolute;left:187px;top:176px;width:520px;font-family:"Cinzel",serif;font-weight:600;font-size:43px;line-height:48px;color:var(--white)}
.hero p{position:absolute;left:187px;top:329px;width:350px;font-size:11px;line-height:17px;color:var(--white)}
.social{position:absolute;left:42px;display:flex;flex-direction:column;gap:16px}
.social span{width:12px;height:12px;border-radius:50%;background:var(--white);display:block}
.slides{position:absolute;top:513px;display:flex;gap:36px;font-family:"Cinzel",serif;font-weight:600;font-size:17px;color:var(--white)}
.slides .on{border-bottom:1.5px solid var(--white)}

/* why */
.callout li{list-style:none;font-size:12px;line-height:18.5px;color:var(--muted);padding-left:12px;position:relative}
.callout li::before{content:"";position:absolute;left:0;top:8px;width:3px;height:3px;border-radius:50%;background:var(--muted)}
.callout b{color:var(--brand);font-weight:600}

/* projects */
.card{position:absolute;overflow:hidden}
.card .label{position:absolute;left:0;right:0;bottom:32px;text-align:center;font-family:"Cinzel",serif;font-weight:600;font-size:17px;line-height:19px;color:var(--white)}
.dots{position:absolute;top:2562px;left:0;width:1200px;display:flex;justify-content:center;gap:26px}
.dots span{width:11px;height:11px;border-radius:50%;background:#dfe3e8}
.dots .on{background:var(--white);border:2px solid var(--brand-soft);box-shadow:inset 0 0 0 2px var(--white);background-color:var(--brand)}

/* recent */
.tabs{position:absolute;left:360px;width:480px;top:2898px;display:flex;justify-content:center;gap:18px;font-size:10px;font-weight:500;color:var(--ink);align-items:center}
.tabs i{width:5px;height:5px;border-radius:50%;background:var(--brand-soft);display:block}
.sub{position:absolute;left:350px;width:500px;text-align:center;font-family:"Cinzel",serif;font-weight:600;font-size:15px;color:var(--ink)}
.sub-text{position:absolute;left:360px;width:480px;text-align:center;font-size:11.5px;line-height:18.2px;color:var(--muted)}

/* footer */
.footer{top:4421px;height:340px;background:var(--footer);color:var(--white)}
.footer h4{font-family:"Cinzel",serif;font-weight:600;font-size:17px}
.footer ul{list-style:none}
.footer li{font-size:11px;line-height:27px}
.form{position:absolute;left:664px;top:76px;width:347px;height:187px;background:var(--footer-box);padding:26px 32px}
.form .field{font-size:8.5px;color:#c9c9c9;border-bottom:1px solid #444;padding-bottom:6px;margin-bottom:16px}
</style>
</head>
<body>

<header class="hero">
  <div class="photo" role="img" aria-label="Aerial view of an industrial site with a headframe tower and brick buildings" style="inset:0;background:linear-gradient(160deg,#6d829b 0%,#4e6684 50%,#2d4463 100%)"></div>
  <div class="shade"></div>
  <div class="logo abs" style="left:187px;top:26px">CRESTLINE14</div>
  <nav class="nav">
    <span class="on">Home</span><span>Why St. Paul</span><span>Lot Layout</span><span>Contact</span>
  </nav>
  <div class="abs" style="left:47px;top:190px;width:1px;height:120px;background:rgba(255,255,255,.5)"></div>
  <div class="social" style="top:344px"><span></span><span></span><span></span></div>
  <h1>Unlock Growth Opportunities in St. Paul, Alberta</h1>
  <p>A thriving hub for businesses, strategically located with unparalleled economic potential and a strong community foundation.</p>
  <div class="btn btn-soft" style="left:187px;top:406px;width:155px;height:29px">Learn More
    <svg viewBox="0 0 18 8"><path d="M0 4h16M13 1l3 3-3 3" stroke="#fff" fill="none" stroke-width="1"/></svg></div>
  <div class="abs" style="left:187px;top:509px;display:flex;align-items:center;gap:12px;color:var(--white)">
    <div style="width:28px;height:28px;border-radius:50%;border:1px solid rgba(255,255,255,.7);display:flex;align-items:center;justify-content:center">
      <svg width="12" height="12" viewBox="0 0 24 24"><path d="M6.6 10.8a15 15 0 006.6 6.6l2.2-2.2c.3-.3.7-.4 1-.2 1.1.4 2.3.6 3.6.6.6 0 1 .4 1 1V20c0 .6-.4 1-1 1A17 17 0 013 4c0-.6.4-1 1-1h3.5c.6 0 1 .4 1 1 0 1.3.2 2.5.6 3.6.1.3 0 .7-.2 1z" fill="#fff"/></svg>
    </div>
    <div><div style="font-size:8.5px">Call Or Text</div><div class="serif" style="font-weight:700;font-size:16px;line-height:18px">555.014.2290</div></div>
  </div>
  <div class="slides" style="left:812px"><span>01</span><span class="on">02</span><span>03</span></div>
  <svg class="abs" style="left:1108px;top:521px" width="42" height="10" viewBox="0 0 42 10"><path d="M5 1L1 5l4 4M37 1l4 4-4 4" stroke="#fff" fill="none" stroke-width="1.2"/></svg>
</header>

<section style="top:562px;height:660px">
  <h2 class="title abs" style="left:0;width:1200px;top:66px">About Us</h2>
  <p class="body abs" style="left:240px;width:720px;top:122px;text-align:center">The property is located on the west side of the Town of St. Paul, a growing municipality located northeast of Edmonton, with a regional population of 13,649. The area has a very strong local economy due to its location between Edmonton and Cold Lake, but with a stronger agricultural base. It serves as the focal point for the Smoky Lake area, with an unemployment rate of 5.0% lower than the provincial average of 8.2%.</p>
  <div class="photo" role="img" aria-label="Regional road map showing the park location and surrounding towns" style="left:186px;top:226px;width:828px;height:289px;border:2px solid #6f9fd8;background:linear-gradient(135deg,#e8efe6 0%,#dfe8ee 50%,#e6ede3 100%)"></div>
  <div class="btn btn-dark" style="left:380px;top:555px;width:192px;height:30px">Learn More About Us
    <svg viewBox="0 0 18 8"><path d="M0 4h16M13 1l3 3-3 3" stroke="#fff" fill="none" stroke-width="1"/></svg></div>
  <div class="vsep" style="left:588px;top:559px"></div>
  <div class="email" style="left:607px;top:555px">
    <div class="ring"><svg width="12" height="9" viewBox="0 0 12 9"><rect x=".5" y=".5" width="11" height="8" fill="none" stroke="#0b55ad"/><path d="M.5.5L6 5l5.5-4.5" fill="none" stroke="#0b55ad"/></svg></div>
    <div><small>Email Us At</small><strong>info@crestline14.com</strong></div>
  </div>
</section>

<section style="top:1220px;height:680px">
  <div class="abs" style="left:468px;top:0;width:732px;height:679px;background:var(--panel)"></div>
  <div class="photo" role="img" aria-label="City street with glass high-rise towers and a construction crane" style="left:0;top:41px;width:490px;height:596px;background:linear-gradient(180deg,#aebfcf 0%,#8294a8 45%,#55665a 80%,#3f5a3a 100%)"></div>
  <h2 class="serif abs" style="left:566px;top:64px;width:560px;font-weight:600;font-size:37px;line-height:48px;color:var(--ink)">Why St. Paul is Your Next Big Opportunity</h2>
  <p class="body abs" style="left:566px;top:163px;width:452px;font-size:11.5px;line-height:18.2px">Located in the County of St. Paul business area, which is currently short of product for sale or lease in both residential and commercial real estate. The area is also in a current influx of population due to its close proximity to the development occurring in the Industrial Heartland. The County of St. Paul is a designated community under the Rural Renewal Stream (RRS) of the Alberta Advantage Immigration Program.</p>
  <div class="serif abs" style="left:566px;top:290px;font-weight:700;font-size:15px">Callout Statistics :</div>
  <ul class="callout abs" style="left:573px;top:322px">
    <li>Regional Population: <b>13,649</b></li>
    <li>Unemployment Rate: <b>5.0%</b> (Lower than Alberta’s average of 8.2%)</li>
    <li>Proximity to Major Projects: <b>Solar, Wind, Carbon Capture Initiatives</b></li>
  </ul>
  <div class="photo" role="img" aria-label="Small map of St. Paul and nearby project sites" style="left:565px;top:401px;width:292px;height:137px;border:2px solid #2c5fa2;background:linear-gradient(135deg,#e9eee8,#dde6ee)"></div>
  <div class="btn btn-soft" style="left:566px;top:576px;width:225px;height:30px">Learn More About St. Paul
    <svg viewBox="0 0 18 8"><path d="M0 4h16M13 1l3 3-3 3" stroke="#fff" fill="none" stroke-width="1"/></svg></div>
  <div class="vsep" style="left:808px;top:580px"></div>
  <div class="email" style="left:827px;top:576px">
    <div class="ring"><svg width="12" height="9" viewBox="0 0 12 9"><rect x=".5" y=".5" width="11" height="8" fill="none" stroke="#0b55ad"/><path d="M.5.5L6 5l5.5-4.5" fill="none" stroke="#0b55ad"/></svg></div>
    <div><small>Email Us At</small><strong>info@crestline14.com</strong></div>
  </div>
</section>

<section style="top:1900px;height:751px">
  <h2 class="title abs" style="left:0;width:1200px;top:62px;font-size:37px">Major Projects in St. Paul<br>Service Area</h2>
  <p class="body abs" style="left:330px;width:540px;top:165px;text-align:center;font-size:11.5px">Lorem Ipsum is simply dummy text of the printing and typesetting industry. Lorem Ipsum has been the industry's standard dummy text ever since the 1500s.</p>
  <div class="card" role="img" aria-label="Aerial view of an open-pit mine" style="left:187px;top:235px;width:265px;height:391px;clip-path:polygon(0 0,100% 0,100% 100%,0 95%);background:linear-gradient(160deg,#6a7f98,#3f5570)"></div>
  <div class="card" role="img" aria-label="Solar panel field under a cloudy sky" style="left:468px;top:235px;width:264px;height:389px;background:linear-gradient(180deg,#dfe6ee 0%,#9eb1c6 40%,#3e5470 65%,#2f4a2a 100%)">
    <div class="label">Ridgeway Solar<br>Project</div></div>
  <div class="card" role="img" aria-label="Aerial view of an industrial processing facility" style="left:748px;top:235px;width:265px;height:391px;clip-path:polygon(0 0,100% 5%,100% 100%,0 100%);background:linear-gradient(160deg,#7d8c9c,#4c5e72)"></div>
</section>
<div class="dots"><span></span><span></span><span class="on"></span><span></span><span></span></div>

<section style="top:2651px;height:991px">
  <div class="abs" style="left:0;top:0;width:1200px;height:991px;background:var(--panel)"></div>
  <div class="photo" role="img" aria-label="Tall residential tower under construction beside a tram street" style="left:0;top:0;width:311px;height:991px;background:linear-gradient(180deg,#8ea5bf 0%,#7d8fa3 40%,#4a5663 75%,#3a3f44 100%)"></div>
  <div class="photo" role="img" aria-label="Aerial view of a neighbourhood with apartment blocks and autumn trees" style="left:888px;top:0;width:312px;height:991px;background:linear-gradient(180deg,#c4d3e2 0%,#8fa2b2 30%,#6d7d6a 60%,#8a6b3c 100%)"></div>
</section>
<h2 class="title abs" style="left:350px;width:500px;top:2740px;font-size:37px">Recent Commercial Developments or Expansions</h2>
<div class="abs" style="left:360px;top:2886px;width:480px;height:1px;background:#b9c4d2"></div>
<div class="tabs"><span>Marchand &amp; Sons Implements Ltd</span><i></i><span>Fieldcrest</span><i></i><span>Northline Heavy Equipment</span></div>
<div class="sub" style="top:2958px">Development Plans :</div>
<p class="sub-text" style="top:2986px">It is currently anticipated that the process of sub-dividing the property and installing the required services to allow for sub-division will take 18 months to complete. The developer is proposing to develop the industrial park to include a truck/RV service centre including a restaurant, a truck/RV car wash and three buildings with 6 bays of office warehouse condos averaging 2,400 square feet per bay. These units will be offered for sale or lease. Presently there is no available space of this nature in the area.</p>
<div class="sub" style="top:3142px">Industrial Condominium Complex</div>
<p class="sub-text" style="top:3172px">Upon re-zoning and sub-division, the project will move forward with construction on as many as three industrial office warehouses. Each of these buildings will consist of a building footprint of roughly 14,500 SF and 6 individually titled units as part of a condo complex. Each building will be situated with highway frontage to maximize exposure, and yard space in the rear. The developer has found this to be the ideal product for small to medium-sized businesses, which is currently lacking in the St Paul market. They have built a similar project in Sherwood Park, Alberta known as The Northgate Business Condominiums.</p>
<div class="sub" style="top:3364px">Existing Shop</div>
<p class="sub-text" style="top:3392px">The existing shop will be parcelled together with a storage yard and sold as is. This will allow for the shop to be purchased or leased along with 2-3 acres of gravelled and fenced yard space.<br>Upon sub-division, the developers intend to sell this property for an estimated price of $1,400,000. This property is presently being leased and a Letter of Intent to purchase has been agreed to by the</p>
<div class="btn btn-soft" style="left:523px;top:3534px;width:155px;height:29px">Learn More
  <svg viewBox="0 0 18 8"><path d="M0 4h16M13 1l3 3-3 3" stroke="#fff" fill="none" stroke-width="1"/></svg></div>

<section style="top:3642px;height:779px">
  <h2 class="title abs" style="left:0;width:1200px;top:92px;font-size:37px">Appraisal Lot<br>Layout</h2>
  <p class="body abs" style="left:230px;width:740px;top:193px;text-align:center;font-size:11.5px">The property is located on the west side of the Town of St. Paul, a growing municipality located northeast of Edmonton, with a regional population of 13,649. The area has a very strong local economy due to its location between Edmonton and Cold Lake, but with a stronger agricultural base. It serves as the focal point for the Smoky Lake area, with an unemployment rate of 5.0% lower than the provincial average of 8.2%.</p>
  <div class="photo" role="img" aria-label="Aerial photo of the site overlaid with the numbered subdivision lot plan" style="left:187px;top:293px;width:826px;height:342px;background:linear-gradient(135deg,#6b5a4a 0%,#7e6a56 40%,#6a7b86 60%,#5d5042 100%)"></div>
  <div class="btn btn-dark" style="left:440px;top:674px;width:138px;height:30px">Contact Us
    <svg viewBox="0 0 18 8"><path d="M0 4h16M13 1l3 3-3 3" stroke="#fff" fill="none" stroke-width="1"/></svg></div>
  <div class="vsep" style="left:596px;top:678px"></div>
  <div class="email" style="left:615px;top:674px">
    <div class="ring"><svg width="12" height="9" viewBox="0 0 12 9"><rect x=".5" y=".5" width="11" height="8" fill="none" stroke="#0b55ad"/><path d="M.5.5L6 5l5.5-4.5" fill="none" stroke="#0b55ad"/></svg></div>
    <div><small>Email Us At</small><strong>info@crestline14.com</strong></div>
  </div>
</section>

<footer class="footer">
  <div class="logo abs" style="left:187px;top:74px;font-size:24px">CRESTLINE14</div>
  <p class="abs" style="left:187px;top:114px;width:200px;font-size:10.5px;line-height:18px;color:#e5e5e5">Lorem Ipsum is simply dummy text of the printing and typesetting industry. Lorem Ipsum has been the industry's standard dummy text ever since the 1500s, when an unknown printer</p>
  <h4 class="abs" style="left:466px;top:76px">Quick Links</h4>
  <ul class="abs" style="left:466px;top:107px"><li>Home</li><li>Why St. Paul</li><li>Lot Layout</li><li>Contact</li></ul>
  <div class="form">
    <div style="font-size:13px;font-weight:600;margin-bottom:14px">LET'S CONNECT!</div>
    <div class="field">Email Address</div>
    <div class="field">Full Name</div>
    <div style="display:flex;align-items:center;gap:6px;font-size:6.5px;color:#bbb;margin-bottom:10px"><span style="width:6px;height:6px;border:1px solid #888;display:block"></span>I agree to the terms &amp; conditions</div>
    <div style="background:var(--brand-soft);height:24px;display:flex;align-items:center;justify-content:center;font-size:9px;font-weight:600">KEEP ME UPDATED</div>
  </div>
  <div class="abs" style="left:0;top:317px;width:1200px;text-align:center;font-size:10.5px;font-weight:500">Copyright@2024-All Rights Reserved</div>
</footer>

</body>
</html>
```